依頼詳細
弊社オリジナルのコンセプト企画住宅をプロデュースするにあたり
お客様にお渡しする資料として使用するリーフレットの制作をお願いします。
「樹影」にはまだカタログやパンフレットが無いので、このリーフレットがお客様への最初のご案内・ご紹介になります。
記載項目
松葉建築株式会社 代表取締役 堀内宗一 お問合せ 0297-61-3027 sora@matsuba-kenchiku.jp
サイズ
A3
ページ数
両面
希望イメージ
シンプル 複雑
単色 カラフル
暗い 明るい
日常 高級
遊び心 厳粛
未来的 伝統的
女性的 男性的
希望する色
納品ファイル
• イラストレーター形式 (.ai)
補足説明
下記のフォルダに、必要なファイルを入れました。
https://files.hokuyo-share.net/f/7Qp2XkLm9RtVw4Zc8Nd3sJb6Hy1Ga5Ue?mode=view
■ 選んだ理由

ご提案いただいた中には、メッセージで協調してくれたいいご提案もあったのですが、内容ボリュームが薄い中で、内容に充実感が感じられたり、その内容とページに集中できる設計になっていたので、読んでいただけるのかなと思いまして選びました

インパクトがあったので決めました。

■ 提案者全員のお礼・コメント

皆さま、ご提案ありがとうございました。 今後もあらたなコンセプトで様々な広告をお願いしようと思っておりますので、どうぞよろしくお願いします!

```html
<!DOCTYPE html>
<html lang="ja">
<head>
<meta charset="utf-8">
<title>樹影 リーフレット</title>
<link rel="stylesheet" href="https://fonts.googleapis.com/css2?family=Yuji+Boku&family=Cormorant+Garamond:wght@500&family=Noto+Sans+JP:wght@400&display=swap">
<style>
  :root {
    --ink: #000000;
    --gold: #d9b13a;
    --gold-light: #f3d472;
    --gold-deep: #a87a1c;
    --foliage: #2a2320;
    --foliage-edge: #120e0c;
    --dusk-top: #6b4a63;
    --dusk-mid: #9a6a7a;
    --house: #3a2a26;
    --caption: #8a8a8a;
  }
  html, body {
    margin: 0;
    padding: 0;
    width: 848px;
    height: 1200px;
    overflow: hidden;
    background: var(--ink);
  }
  .leaflet {
    position: relative;
    width: 848px;
    height: 1200px;
    background: var(--ink);
    overflow: hidden;
  }
  .tree-canopy {
    position: absolute;
    left: 0;
    top: 0;
    width: 600px;
    height: 380px;
    background: radial-gradient(ellipse 70% 75% at 25% 20%, var(--foliage) 0%, var(--foliage-edge) 60%, transparent 100%);
  }
  .gold-spatter {
    position: absolute;
    border-radius: 50%;
    background: radial-gradient(ellipse at center, rgba(217,177,58,0.35) 0%, rgba(217,177,58,0.12) 45%, transparent 75%);
  }
  .gold-spatter--upper { left: 470px; top: 150px; width: 300px; height: 170px; }
  .gold-spatter--lower { left: 150px; top: 420px; width: 280px; height: 150px; }
  .title {
    position: absolute;
    left: 300px;
    top: 190px;
    width: 220px;
    margin: 0;
    font-family: "Yuji Boku", serif;
    font-weight: 400;
    font-size: 190px;
    line-height: 1;
    color: var(--gold);
    background: linear-gradient(160deg, var(--gold-light) 0%, var(--gold) 50%, var(--gold-deep) 100%);
    -webkit-background-clip: text;
    background-clip: text;
    -webkit-text-fill-color: transparent;
  }
  .title__char { display: block; }
  .title__char--second { margin-top: 70px; }
  .title-roman {
    position: absolute;
    left: 440px;
    top: 418px;
    margin: 0;
    font-family: "Cormorant Garamond", serif;
    font-weight: 500;
    font-size: 26px;
    letter-spacing: 4px;
    color: #e6e0cf;
  }
  .exterior-photo {
    position: absolute;
    left: 395px;
    top: 840px;
    width: 453px;
    height: 320px;
    background:
      linear-gradient(180deg, transparent 55%, var(--house) 75%, #1a1210 100%),
      linear-gradient(180deg, var(--dusk-top) 0%, var(--dusk-mid) 50%, #c08a8a 70%);
    -webkit-mask-image: radial-gradient(ellipse 95% 90% at 70% 60%, #000 55%, transparent 100%);
    mask-image: radial-gradient(ellipse 95% 90% at 70% 60%, #000 55%, transparent 100%);
  }
  .caption {
    position: absolute;
    right: 20px;
    top: 1168px;
    margin: 0;
    font-family: "Noto Sans JP", sans-serif;
    font-size: 10px;
    color: var(--caption);
  }
</style>
</head>
<body>
  <main class="leaflet">
    <div class="tree-canopy" role="img" aria-label="夜空に広がる樹木の枝葉のシルエット"></div>
    <div class="gold-spatter gold-spatter--upper" role="img" aria-label="金色の墨はねの装飾"></div>
    <div class="gold-spatter gold-spatter--lower" role="img" aria-label="金色の墨はねの装飾"></div>
    <h1 class="title">
      <span class="title__char">樹</span>
      <span class="title__char title__char--second">影</span>
    </h1>
    <p class="title-roman">JUEI</p>
    <div class="exterior-photo" role="img" aria-label="夕暮れの空の下に建つ平屋住宅の外観"></div>
    <p class="caption">※掲載の外観写真はイメージです。実際とは異なる場合があります。</p>
  </main>
</body>
</html>
```